Visitenkarten-Design für Hausarztpraxis
Zielgruppe
Hausarztpraxis mit Schwerpunkt Geriatrie
Zielgruppe: Patienten in einem eher ländlichen Stadtgebiet mit hoher Anzahl von Senioren
Aufgabenstellung
Idee: Kombination eines Gutscheines für eine Kaffespezialität auf der Rückseite und einer beschreibbaren Vorderseite als Bestellkärtchen mit Foto von zukünftigen "Praxisgängern" im Querschnitt. D.h. Zu sehen sein sollten 1 lustige Oma , 1 lustiger Opa (z.B. Pfeife rauchend), 1 Jugendlicher und diverse andere Erwachsene verschiedener Berufsgruppen. Beispielhaft siehe unter: Tintenfuchs: Online Terminvereinbarung-Die keine Wünsche offen lässt. Das Bild könnte auch "gezeichnet" sein. Ich würde aber ein treffendes Foto bevorzugen. Design: gut leserliche Schrift, keine verschlungene Schriftarten, wegen Lesbarkeit für Renterklientel.
Info auf der Vorderseite mit Foto: WARTEN? Nicht bei uns - Ihr persönlicher Wunschtermin:
Info auf der Rückseite (Gutschein): Gutschein für eine Kaffeespezialität (Kaffeesymbol)
farblich unterlegt, Farbe egal, passend abgestimmt zur Vorderseite
Zur Erklärung:
Die Form/ Grösse sollte die einer Visitenkarte möglichst nicht überschreiten. Gern auch eine grössere Visitenkartenform 10cm breit und 7,5 cm hoch. Das Format ist unserem Zeitdruck geschuldet. Es muss ein Werbemittel in 14 Tagen zur Praxiseröffnung zur Verfügung stehen, was sich schnell und kostengünstig produzieren und bei Bedarf ohne Probleme nachproduzieren lässt.
Sonderformate haben lange Auftragszeiten bei den auszuführenden Werbedruckfirmen.

```html
<!DOCTYPE html>
<html lang="de">
<head>
<meta charset="utf-8">
<title>Visitenkarte Hausarztpraxis – Terminkarte und Gutschein</title>
<link rel="stylesheet" href="https://fonts.googleapis.com/css2?family=Didact+Gothic&display=swap">
<style>
  :root {
    --teal: #044a63;
    --white: #ffffff;
    --page: #ffffff;
    --shadow: rgba(0, 0, 0, 0.35);
  }
  html, body {
    margin: 0;
    padding: 0;
    width: 849px;
    height: 1200px;
    overflow: hidden;
    background: var(--page);
  }
  .sheet {
    position: relative;
    width: 849px;
    height: 1200px;
  }
  .card {
    position: absolute;
    left: 73px;
    width: 687px;
    height: 445px;
    filter: drop-shadow(3px 4px 4px var(--shadow));
  }
  .card--front { top: 60px; }
  .card--back { top: 643px; }
  .card svg { display: block; width: 100%; height: 100%; }
  .type {
    font-family: "Didact Gothic", "Century Gothic", sans-serif;
  }
  .fill-teal { fill: var(--teal); }
  .fill-white { fill: var(--white); }
</style>
</head>
<body>
<main class="sheet">

  <!-- Vorderseite: Terminkarte -->
  <section class="card card--front" aria-label="Terminkarte Vorderseite">
    <svg viewBox="0 0 1004 650" xmlns="http://www.w3.org/2000/svg">
      <defs>
        <linearGradient id="tone-warm" x1="0" y1="0" x2="0" y2="1">
          <stop offset="0" stop-color="#d9d1c8"/>
          <stop offset="1" stop-color="#b9cfc9"/>
        </linearGradient>
        <linearGradient id="tone-light" x1="0" y1="0" x2="0" y2="1">
          <stop offset="0" stop-color="#e4e4e4"/>
          <stop offset="1" stop-color="#5f7a99"/>
        </linearGradient>
        <linearGradient id="tone-blue" x1="0" y1="0" x2="0" y2="1">
          <stop offset="0" stop-color="#9cc1c8"/>
          <stop offset="1" stop-color="#d4d4d0"/>
        </linearGradient>
        <linearGradient id="tone-grey" x1="0" y1="0" x2="0" y2="1">
          <stop offset="0" stop-color="#e2e2e2"/>
          <stop offset="1" stop-color="#8e8e8e"/>
        </linearGradient>
      </defs>

      <rect class="fill-white" x="0" y="0" width="1004" height="650"/>

      <!-- Kopfzeile -->
      <polygon class="fill-teal" points="538,0 1004,0 1004,155 525,155"/>
      <text class="type fill-teal" x="51" y="116" font-size="88">WARTEN?</text>
      <text class="type fill-white" x="563" y="110" font-size="62">Nicht bei uns</text>

      <!-- Fotostreifen -->
      <g role="img" aria-label="Foto: ältere Frau mit erhobenen Daumen">
        <rect x="0" y="155" width="266" height="326" fill="url(#tone-warm)"/>
      </g>
      <g role="img" aria-label="Foto: lächelnder Jugendlicher mit verschränkten Armen">
        <polygon points="266,155 525,155 500,481 266,481" fill="url(#tone-light)"/>
      </g>
      <g role="img" aria-label="Foto: lachender älterer Herr mit Bart">
        <polygon points="525,155 773,155 773,481 500,481" fill="url(#tone-blue)"/>
      </g>
      <g role="img" aria-label="Foto: jubelnde junge Frau">
        <rect x="773" y="155" width="231" height="326" fill="url(#tone-grey)"/>
      </g>

      <!-- Fußzeile -->
      <polygon class="fill-teal" points="0,481 498,481 485,650 0,650"/>
      <text class="type fill-white" font-size="44">
        <tspan x="111" y="548">Ihr persönlicher</tspan>
        <tspan x="111" y="600">Wunschtermin</tspan>
      </text>
      <text class="type fill-teal" font-size="40">
        <tspan x="565" y="546">Datum:</tspan>
        <tspan x="565" y="602">Uhrzeit:</tspan>
      </text>
    </svg>
  </section>

  <!-- Rückseite: Gutschein -->
  <section class="card card--back" aria-label="Gutschein Rückseite">
    <svg viewBox="0 0 1004 650" xmlns="http://www.w3.org/2000/svg">
      <defs>
        <linearGradient id="tone-coffee" x1="0" y1="0" x2="0.4" y2="1">
          <stop offset="0" stop-color="#6b5a4c"/>
          <stop offset="0.5" stop-color="#4a3326"/>
          <stop offset="1" stop-color="#2c1a10"/>
        </linearGradient>
      </defs>

      <g role="img" aria-label="Foto: dampfende Tasse Kaffee mit Kaffeebohnen und Kaffeemühle">
        <rect x="0" y="0" width="1004" height="650" fill="url(#tone-coffee)"/>
      </g>
      <polygon class="fill-teal" points="0,0 541,0 486,650 0,650"/>

      <text class="type fill-white" x="51" y="232" font-size="90">Gutschein</text>
      <text class="type fill-white" font-size="56">
        <tspan x="51" y="370">für eine</tspan>
        <tspan x="51" y="440">Kaffespezialität</tspan>
      </text>
    </svg>
  </section>

</main>
</body>
</html>
```